Business Card/Email Signature design

We need an new business card design for our business as well as an animated email signature design.<br/>Business Card:<br/>The business card designs need to have the following information for each director:<br/>Glen Purvis<br/>Managing Director<br/>glen@fernloxstaffing.com.au<br/>0468203917<br/>www.fernloxstaffing.com.au<br/><br/>and<br/><br/>Rosalind Tremby<br/>Director<br/>rosalind@fernloxstaffing.com.au<br/>0457390264<br/>www.fernloxstaffing.com.au<br/><br/>I will upload the Fernlox. Staffing logo designs to be used for the design. Our colours are black and white. I would like to see the designs in both coloured backgrounds.<br/><br/>For the email signature we need the same information. I also need to add a logo of our association NPLB of which i will add the logo as well. This NPLB logo does not need to be used for the business card unless it works with the design.<br/>For the animation part of the logo our company is called Fernlox. Staffing - We have a number of divisions called Fernlox. Construct, Fernlox. Property, Fernlox. Sales, Fernlox. Executive Support, Fernlox. Private PA, Fernlox. Talent and Fernlox. Coaching<br/>I would like for the email Signature to be designed so that the Fernlox. stays still but the words Construct, Property, Sales, Executive Support, Private PA, Talent and Coaching rotate through to capture attention and tell the story of what we do.<br/><br/>Any questions please don't hesitate to message me.

Industry/Entity Type

Recruiter

Contact Information for Business Card

Glen Purvis
Managing Director
glen@fernloxstaffing.com.au
0468203917
www.fernloxstaffing.com.au

Rosalind Tremby
Director
rosalind@fernloxstaffing.com.au
0457390264
www.fernloxstaffing.com.au

Font styles to use
Serif

Colors

Designer to choose colors to be used in the design.

Requirements
Must have
• The animation for the email signature as described
Should not have
• Any changes to my logo. Any colour other that black or white

```html
<!DOCTYPE html>
<html lang="en">
<head>
<meta charset="utf-8">
<title>Fernlox. Staffing — Business Card</title>
<link href="https://fonts.googleapis.com/css2?family=Work+Sans:wght@400;500&display=swap" rel="stylesheet">
<style>
  :root {
    --stage: #1b1b1b;
    --card: #161616;
    --card-edge: #262626;
    --ink: #f4f4f4;
    --ink-soft: #d9d9d9;
  }
  * { margin: 0; padding: 0; box-sizing: border-box; }
  html, body {
    width: 1200px; height: 900px; overflow: hidden;
    background: var(--stage);
    font-family: "Work Sans", sans-serif;
    color: var(--ink);
  }
  .sheet {
    width: 1200px; height: 900px;
    display: flex; flex-direction: column;
    align-items: center; justify-content: center;
    gap: 40px;
  }
  .card {
    width: 640px; height: 390px;
    background: linear-gradient(135deg, #121212 0%, #1c1c1c 60%, #242424 100%);
    border: 1px solid var(--card-edge);
    position: relative;
  }
  .brand {
    display: flex; align-items: center; gap: 18px;
  }
  .brand-mark {
    width: 26px; height: 26px;
    border: 2px solid var(--ink);
    flex: none;
  }
  .brand-name {
    font-weight: 500;
    letter-spacing: 0.06em;
    color: var(--ink);
    white-space: nowrap;
  }
  .card-front {
    display: flex; align-items: center; justify-content: center;
  }
  .card-front .brand-name { font-size: 34px; }
  .card-front .brand-mark { width: 34px; height: 34px; }

  .card-back {
    display: flex; align-items: center;
    padding: 0 44px;
  }
  .card-back .brand {
    width: 200px; flex-direction: column; align-items: flex-start; gap: 12px;
  }
  .card-back .brand-name { font-size: 22px; white-space: normal; line-height: 1.25; }
  .divider {
    width: 1px; height: 150px;
    background: var(--ink-soft);
    margin: 0 36px 0 10px;
  }
  .person-name {
    font-size: 30px; font-weight: 500;
    letter-spacing: 0.08em; text-transform: uppercase;
  }
  .person-role {
    font-size: 16px; letter-spacing: 0.04em;
    color: var(--ink-soft);
    margin-top: 2px;
  }
  .contact-list {
    list-style: none;
    margin-top: 22px;
    font-size: 16px; letter-spacing: 0.03em;
  }
  .contact-list li {
    display: flex; align-items: center; gap: 9px;
    line-height: 1.55;
  }
  .contact-list svg { width: 12px; height: 12px; flex: none; }
</style>
</head>
<body>
<main class="sheet">
  <section class="card card-front" aria-label="Card front">
    <div class="brand">
      <span class="brand-mark"></span>
      <span class="brand-name">Fernlox. Staffing</span>
    </div>
  </section>

  <section class="card card-back" aria-label="Card back">
    <div class="brand">
      <span class="brand-mark"></span>
      <span class="brand-name">Fernlox. Staffing</span>
    </div>
    <span class="divider"></span>
    <div class="person">
      <h1 class="person-name">Glen Purvis</h1>
      <p class="person-role">Managing Director</p>
      <ul class="contact-list">
        <li>
          <svg viewBox="0 0 12 12" aria-hidden="true"><path d="M3 1 L5 3.5 L4 4.8 Q5 7 7.2 8 L8.5 7 L11 9 L9.8 11 Q5 11 1 3 Z" fill="#f4f4f4"/></svg>
          0468203917
        </li>
        <li>
          <svg viewBox="0 0 12 12" aria-hidden="true"><rect x="1" y="2.5" width="10" height="7" fill="none" stroke="#f4f4f4" stroke-width="1.2"/><path d="M1 2.5 L6 6.5 L11 2.5" fill="none" stroke="#f4f4f4" stroke-width="1.2"/></svg>
          glen@fernloxstaffing.com.au
        </li>
        <li>
          <svg viewBox="0 0 12 12" aria-hidden="true"><circle cx="6" cy="6" r="5" fill="none" stroke="#f4f4f4" stroke-width="1.1"/><ellipse cx="6" cy="6" rx="2.2" ry="5" fill="none" stroke="#f4f4f4" stroke-width="1"/><path d="M1 6 H11" stroke="#f4f4f4" stroke-width="1"/></svg>
          www.fernloxstaffing.com.au
        </li>
      </ul>
    </div>
  </section>
</main>
</body>
</html>
```